Business Card Design Project

We need a business card designed for a new Luxury Custom Homebuilding company based in Arizona. We previous were called "Belcrest Estates" but want to start using "Belcrest Custom Homes" We want the message to communicate high end, luxury and cutting-edge. We like the blue, white and black color scheme.
Belcrest Custom Homes
Marcus T. Halloway
Chief Executive Officer
Office: 480-555-0142
Mobile: 480-555-0178
email: marc@belcrestcustom-example.com
web adress: www.BelcrestCustom-example.com
Updates
We have made a change to our website address and email address based on recieving feedback from a nmber of individuals. The feedback was web address and email address was to long. Therefore we have made a change. The new web adress and email adress are the following.
www.BelcrestCustom-example.com
marc@belcrestcustom-example.com
Also I decided against using in yellow. I like the colors blue,black, white and maybe gray.
Target Market(s)
Our target market is the wealthy individuals looking for a luxury high-end custom home.
Industry/Entity Type
Business
Look and feel

```html
<!DOCTYPE html>
<html lang="en">
<head>
<meta charset="utf-8">
<title>Belcrest Custom Homes – Business Card</title>
<link rel="stylesheet" href="https://fonts.googleapis.com/css2?family=Roboto+Condensed:ital,wght@0,400;0,700;1,300;1,400&display=swap">
<style>
  :root {
    --stage-light: #f1f1f3;
    --stage-dark: #d6d6d8;
    --card-blue: #5b9bd5;
    --ink-white: #ffffff;
    --ink-gray: #4f4f51;
  }
  * { box-sizing: border-box; margin: 0; padding: 0; }
  html, body { width: 1200px; height: 1200px; overflow: hidden; }
  body {
    position: relative;
    background: linear-gradient(90deg, var(--stage-dark) 0%, var(--stage-light) 45%, var(--stage-light) 100%);
    font-family: "Roboto Condensed", "Arial Narrow", sans-serif;
    color: var(--ink-white);
  }
  .card {
    position: absolute;
    left: 114px;
    width: 970px;
    height: 553px;
    background: var(--card-blue);
    overflow: hidden;
  }
  .card--front { top: 22px; }
  .card--back { top: 624px; }

  /* Front */
  .front-name {
    position: absolute;
    left: 56px;
    top: 214px;
    line-height: 1;
    font-weight: 700;
    color: var(--ink-white);
  }
  .front-name__main { display: block; font-size: 104px; letter-spacing: -2px; }
  .front-name__sub { display: block; font-size: 37px; margin-top: 2px; padding-left: 140px; letter-spacing: 0.5px; }

  .contact-frame {
    position: absolute;
    left: 541px;
    top: 228px;
    width: 383px;
    height: 275px;
    border-top: 2px solid var(--ink-white);
    border-left: 2px solid var(--ink-white);
  }
  .contact {
    position: absolute;
    left: 583px;
    top: 258px;
    font-size: 23px;
    line-height: 1.4;
  }
  .contact__name { font-weight: 700; font-size: 24px; }
  .contact__title { font-weight: 400; margin-bottom: 24px; }
  .contact__list { list-style: none; font-size: 23px; line-height: 32px; }
  .contact__label { display: inline-block; width: 40px; }

  /* Back */
  .back-name {
    position: absolute;
    left: 22px;
    top: 112px;
    font-weight: 700;
    color: var(--ink-white);
    line-height: 1;
  }
  .back-name__main { display: block; font-size: 262px; letter-spacing: -6px; }
  .back-name__sub { display: block; font-size: 74px; margin-top: -4px; padding-left: 312px; letter-spacing: 1px; }

  .web {
    position: absolute;
    right: 32px;
    bottom: 30px;
    font-size: 40px;
    line-height: 1;
  }
  .web__affix { font-style: italic; font-weight: 300; }
  .web__brand { font-weight: 700; }
  .web__suffix { font-weight: 700; color: var(--ink-gray); }
</style>
</head>
<body>

<section class="card card--front" aria-label="Card front">
  <div class="front-name">
    <span class="front-name__main">Belcrest</span>
    <span class="front-name__sub">CUSTOM HOMES</span>
  </div>

  <div class="contact-frame"></div>
  <div class="contact">
    <p class="contact__name">Marcus T. Halloway</p>
    <p class="contact__title">Chief Executive Officer</p>
    <ul class="contact__list">
      <li><span class="contact__label">P:</span>480-555-0142</li>
      <li><span class="contact__label">M:</span>480-555-0178</li>
      <li><span class="contact__label">E:</span>marc@belcrestcustom-example.com</li>
      <li><span class="contact__label">W:</span>www.BelcrestCustom-example.com</li>
    </ul>
  </div>
</section>

<section class="card card--back" aria-label="Card back">
  <div class="back-name">
    <span class="back-name__main">Belcrest</span>
    <span class="back-name__sub">CUSTOM HOMES</span>
  </div>
  <p class="web"><span class="web__affix">www.</span><span class="web__brand">Belcrest</span><span class="web__suffix">Custom-example</span><span class="web__affix">.com</span></p>
</section>

</body>
</html>
```